Business card for home developer

Name, email, phone #, logo, address, lic # and slogan.
Slogan to say something like, "Leader in quality neighborhood communities" maybe? The last one said "A sept above the rest". Some thing saying we are above the other people.
The card can be two sided?
Home buyers
Business

```html
<!DOCTYPE html>
<html lang="en">
<head>
<meta charset="utf-8">
<title>Crestline Homes – Business Card</title>
<link rel="stylesheet" href="https://fonts.googleapis.com/css2?family=Exo+2:ital,wght@0,400;0,700;1,400&display=swap">
<style>
  :root {
    --canvas-bg: #ecebe8;
    --brand-blue: #1f3f7c;
    --brand-red: #a5212b;
    --card-white: #f4f4f5;
    --text-grey: #454a52;
    --rule-grey: #cfd1d5;
    --name-light: #e3e5ea;
  }
  * { margin: 0; padding: 0; box-sizing: border-box; }
  html, body {
    width: 1200px; height: 880px; overflow: hidden;
    background: var(--canvas-bg);
    font-family: "Exo 2", sans-serif;
  }
  .canvas { position: relative; width: 1200px; height: 880px; }
  .card {
    position: absolute; top: 286px;
    width: 540px; height: 308px;
    box-shadow: 0 6px 18px rgba(0,0,0,0.18);
    overflow: hidden;
  }

  /* Front */
  .card-front { left: 40px; background: var(--brand-blue); }
  .front-name {
    position: absolute; left: 0; right: 0; top: 118px;
    text-align: center;
    font-size: 46px; font-weight: 700; line-height: 1;
    letter-spacing: 1px; color: var(--name-light);
  }
  .front-web {
    position: absolute; left: 0; right: 0; bottom: 26px;
    text-align: center; color: #ffffff;
    font-size: 18px; letter-spacing: 4px;
  }
  .front-web strong { font-weight: 700; }

  /* Back */
  .card-back { left: 620px; background: var(--card-white); }
  .contact {
    position: absolute; left: 28px; top: 28px; width: 210px;
    color: var(--text-grey);
  }
  .contact-name { font-size: 17px; font-weight: 700; color: var(--brand-blue); }
  .contact-role { font-size: 11px; font-style: italic; margin-bottom: 10px; }
  .contact-group { border-bottom: 1px solid var(--rule-grey); padding: 6px 0 8px; }
  .contact-group:last-child { border-bottom: none; }
  .contact-line {
    display: flex; align-items: flex-start; gap: 9px;
    font-size: 12.5px; line-height: 19px;
  }
  .contact-line svg { flex: 0 0 11px; margin-top: 4px; }
  .back-name {
    position: absolute; right: 30px; top: 118px;
    font-size: 28px; font-weight: 700; line-height: 1;
    color: var(--brand-blue); white-space: nowrap;
  }
  .licence {
    position: absolute; right: 30px; bottom: 26px; text-align: right;
    color: var(--text-grey); font-size: 12.5px;
  }
  .licence-title { font-weight: 700; color: var(--brand-red); font-size: 13px; }
</style>
</head>
<body>
<main class="canvas">

  <section class="card card-front" aria-label="Card front">
    <p class="front-name">CRESTLINE HOMES</p>
    <p class="front-web">www.<strong>domain</strong>.com</p>
  </section>

  <section class="card card-back" aria-label="Card back">
    <div class="contact">
      <p class="contact-name">Name Surname</p>
      <p class="contact-role">manager</p>

      <div class="contact-group">
        <p class="contact-line">
          <svg width="11" height="11" viewBox="0 0 11 11"><rect x="1" y="1" width="9" height="9" rx="1.5" fill="#1f3f7c"/><rect x="3" y="3" width="5" height="2" fill="#f4f4f5"/></svg>
          (+00) 123 456 789
        </p>
        <p class="contact-line">
          <svg width="11" height="11" viewBox="0 0 11 11"><rect x="0.5" y="4" width="10" height="6" rx="1" fill="#1f3f7c"/><rect x="2.5" y="1" width="6" height="3" fill="#1f3f7c"/></svg>
          (+00) 123 456 789
        </p>
        <p class="contact-line">
          <svg width="11" height="11" viewBox="0 0 11 11"><rect x="2.5" y="0.5" width="6" height="10" rx="1.2" fill="#1f3f7c"/><rect x="3.7" y="2" width="3.6" height="5.5" fill="#f4f4f5"/></svg>
          (+00) 123 456 789
        </p>
      </div>

      <div class="contact-group">
        <p class="contact-line">
          <svg width="11" height="11" viewBox="0 0 11 11"><rect x="0.5" y="2" width="10" height="7" rx="1" fill="#1f3f7c"/><path d="M1 2.5 L5.5 6 L10 2.5" stroke="#f4f4f5" stroke-width="1" fill="none"/></svg>
          office@domain.com
        </p>
        <p class="contact-line">
          <svg width="11" height="11" viewBox="0 0 11 11"><circle cx="5.5" cy="5.5" r="4.5" fill="none" stroke="#1f3f7c" stroke-width="1.2"/><path d="M1 5.5 H10 M5.5 1 V10" stroke="#1f3f7c" stroke-width="0.9"/></svg>
          www.domain.com
        </p>
      </div>

      <div class="contact-group">
        <p class="contact-line">
          <svg width="11" height="13" viewBox="0 0 11 13"><path d="M5.5 12.5 C2 8 1 6.5 1 4.8 A4.5 4.5 0 0 1 10 4.8 C10 6.5 9 8 5.5 12.5 Z" fill="#1f3f7c"/><circle cx="5.5" cy="4.8" r="1.6" fill="#f4f4f5"/></svg>
          <span>Your Address Goes Here<br>City, Country, Zipcode</span>
        </p>
      </div>
    </div>

    <p class="back-name">CRESTLINE HOMES</p>

    <div class="licence">
      <p class="licence-title">Licences</p>
      <p>XX 12345, XX 12345</p>
    </div>
  </section>

</main>
</body>
</html>
```